Boulder Grip Supply Business Card Design Challenge

Please create me a simple card using my logo. I'm not looking for anything abstract.
A couple of colours for text and maybe something on the card so the whole card isn't just a white board.
Please send me samples and I'll reply with suggestions to refine the design. Thank you

Reason: The Ormeau address was incorrect in the brief, so I have updated that so the 4 and 5 star submissions can be updated and resubmitted please!!! Sorry and thank you

Target Market(s)

Mining companies and rock producing aggregate companies. Quarries

Industry/Entity Type

Mining

Contact Information for Business Card

Name - Graham Ellsworth / Company Logo AND Boulder Grip Supply Pty Ltd / position - Managing Director / address1 - Unit 3, 14 Tindal Crescent, Ormeau 4208 Queensland AU / address2 - PO Box 917, Oxenford 4210 Queensland AU / mobile - 0427 915 306 / phone - 07 5591 4867 / fax - 07 5591 4803 / email - ge@bouldergripsupply.example.au / website - www.bouldergripsupply.example.au

Requirements
Must have
• Business details as per the above. The phone and fax numbers will be confirmed before the end of the project. Thank you
• SINGLE SIDED ONLY please on Card, not transparent plastic

```html
<!DOCTYPE html>
<html lang="en">
<head>
<meta charset="utf-8">
<title>Boulder Grip Supply – Business Card</title>
<link href="https://fonts.googleapis.com/css2?family=Open+Sans:wght@400;600;700&family=Russo+One&display=swap" rel="stylesheet">
<style>
  :root {
    --bg: #e9e6e1;
    --card: #ffffff;
    --blue: #2aa6e0;
    --blue-soft: #cfe9f6;
    --blue-faint: #e6f4fb;
    --grey: #5b5e62;
    --grey-dark: #4a4d51;
  }
  * { box-sizing: border-box; margin: 0; padding: 0; }
  html, body { width: 1200px; height: 1023px; overflow: hidden; }
  body {
    background: var(--bg);
    font-family: "Open Sans", Arial, sans-serif;
    position: relative;
  }
  .card {
    position: absolute;
    left: 100px; top: 225px;
    width: 1000px; height: 572px;
    background: var(--card);
    overflow: hidden;
    box-shadow: 0 6px 24px rgba(0,0,0,0.12);
  }
  .card__panel {
    position: absolute;
    right: 0; top: 0;
    width: 470px; height: 572px;
    background: linear-gradient(135deg, var(--blue-faint) 0%, var(--blue-soft) 100%);
    clip-path: polygon(30% 0, 100% 0, 100% 100%, 0 100%);
  }
  .brand {
    position: absolute;
    left: 70px; top: 236px;
    display: flex; align-items: center; gap: 18px;
  }
  .brand__square {
    width: 64px; height: 64px;
    background: var(--blue);
  }
  .brand__name {
    font-family: "Open Sans", Arial, sans-serif;
    font-weight: 700;
    font-size: 40px;
    line-height: 1.05;
    color: var(--grey-dark);
    text-transform: uppercase;
    letter-spacing: 1px;
  }
  .details {
    position: absolute;
    left: 500px; top: 70px;
    color: var(--grey);
    font-size: 21px;
    line-height: 1.45;
  }
  .details__name {
    font-family: "Russo One", Arial, sans-serif;
    font-size: 32px;
    color: var(--blue);
    text-transform: uppercase;
    letter-spacing: 2px;
    line-height: 1.1;
  }
  .details__role { font-size: 21px; margin-bottom: 16px; }
  .contact-list { list-style: none; }
  .contact-list li { display: flex; align-items: center; gap: 10px; }
  .icon {
    width: 20px; height: 20px; flex: none;
    background: var(--blue);
    border-radius: 3px;
    display: flex; align-items: center; justify-content: center;
  }
  .icon svg { width: 14px; height: 14px; fill: #fff; }
  .details__company {
    margin-top: 18px;
    color: var(--blue);
    font-weight: 700;
  }
  .address { list-style: none; }
  .address li { display: flex; gap: 10px; }
  .address .icon { margin-top: 6px; }
  .address span { display: block; }
</style>
</head>
<body>
  <div class="card">
    <div class="card__panel" role="img" aria-label="Soft light-blue background panel"></div>

    <div class="brand">
      <div class="brand__square"></div>
      <div class="brand__name">Boulder Grip<br>Supply</div>
    </div>

    <div class="details">
      <div class="details__name">Graham Ellsworth</div>
      <div class="details__role">Managing Director</div>

      <ul class="contact-list">
        <li><span class="icon"><svg viewBox="0 0 14 14"><rect x="4" y="1" width="6" height="12" rx="1"/></svg></span>0427 915 306</li>
        <li><span class="icon"><svg viewBox="0 0 14 14"><path d="M3 1l3 3-1.5 2a8 8 0 0 0 3.5 3.5L10 8l3 3-2 2C6 13 1 8 1 3z"/></svg></span>07 5591 4867</li>
        <li><span class="icon"><svg viewBox="0 0 14 14"><rect x="1" y="5" width="12" height="7" rx="1"/><rect x="3" y="1" width="8" height="4"/></svg></span>07 5591 4803</li>
        <li><span class="icon"><svg viewBox="0 0 14 14"><path d="M1 3h12v8H1z M1 3l6 5 6-5" fill="none" stroke="#fff" stroke-width="1.5"/></svg></span>ge@bouldergripsupply.example.au</li>
        <li><span class="icon"><svg viewBox="0 0 14 14"><circle cx="7" cy="7" r="5.5" fill="none" stroke="#fff" stroke-width="1.4"/><path d="M1.5 7h11M7 1.5v11" stroke="#fff" stroke-width="1.2"/></svg></span>www.bouldergripsupply.example.au</li>
      </ul>

      <div class="details__company">Boulder Grip Supply Pty Ltd</div>
      <ul class="address">
        <li><span class="icon"><svg viewBox="0 0 14 14"><path d="M7 1a4 4 0 0 1 4 4c0 3-4 8-4 8S3 8 3 5a4 4 0 0 1 4-4z"/></svg></span><span>Unit 3, 14 Tindal Crescent<br>Ormeau 4208 Queensland AU</span></li>
        <li><span class="icon"><svg viewBox="0 0 14 14"><path d="M7 1a4 4 0 0 1 4 4c0 3-4 8-4 8S3 8 3 5a4 4 0 0 1 4-4z"/></svg></span><span>PO Box 917 Oxenford<br>4210 Queensland AU</span></li>
      </ul>
    </div>
  </div>
</body>
</html>
```